Finance Company Need Presentation Folder/ Brochure Design

We are a Finance Brokerage Firm in Adelaide, we provide finance for personal, car, equipment, boat and aviation loans. We are looking for designs for new presentation folders that are simplistic, yet professional and classy. We would like them to include the color orange and communicate financial safety and growth.

Target Market(s)

The folders will be going to current and perspective clients

Industry/Entity Type

Finance

Font styles to use
Other font styles liked:
• Raleway or something similar, example attached as 'Opening Keys Evening'

Colors
f37122
ffffff
000000

Requirements
Must have
• Phone Number: 1300 482 917
• Address:
• 47 Warrick Lane
• Brookhaven, SA 5071
• Website: tallowpeak.com.au
Nice to have
• "Experience finance in a whole new way... Experience Tallowpeak"
• Asset Finance - Home Loans - Personal Loans

```html
<!DOCTYPE html>
<html lang="en">
<head>
<meta charset="utf-8">
<title>Tallowpeak – Inner Folder with Closed Pocket</title>
<link rel="stylesheet" href="https://fonts.googleapis.com/css2?family=Raleway:wght@400&family=Roboto:wght@700&display=swap">
<style>
  :root {
    --stage: #616163;
    --panel: #ebebed;
    --panel-shade: #e3e3e6;
    --pocket: #363435;
    --pocket-shade: #2f2d2e;
    --ink-dark: #2b2b35;
    --ink-light: #ffffff;
    --accent: #f37122;
    --label: #ffffff;
  }
  * { margin: 0; padding: 0; box-sizing: border-box; }
  html, body {
    width: 1200px;
    height: 1200px;
    overflow: hidden;
    background: var(--stage);
  }
  .canvas {
    position: relative;
    width: 1200px;
    height: 1200px;
  }
  .view-label {
    position: absolute;
    left: 63px;
    top: 197px;
    font-family: "Roboto", Arial, sans-serif;
    font-weight: 700;
    font-size: 17px;
    letter-spacing: 0.2px;
    color: var(--label);
  }
  .folder-inner {
    position: absolute;
    left: 61px;
    top: 226px;
    width: 1078px;
    height: 748px;
    background: linear-gradient(160deg, var(--panel) 0%, var(--panel-shade) 100%);
    overflow: hidden;
  }
  .pocket {
    position: absolute;
    right: 0;
    bottom: 0;
    width: 521px;
    height: 227px;
    background: linear-gradient(160deg, var(--pocket) 0%, var(--pocket-shade) 100%);
    border-top-left-radius: 72px;
  }
  .brand {
    position: absolute;
    display: flex;
    align-items: flex-start;
    white-space: nowrap;
  }
  .brand-name {
    font-family: "Raleway", Helvetica, sans-serif;
    font-weight: 400;
    letter-spacing: -0.5px;
    line-height: 1;
  }
  .brand-dot {
    border-radius: 50%;
    background: var(--accent);
    flex: none;
  }
  .brand--panel {
    left: 147px;
    top: 354px;
  }
  .brand--panel .brand-name {
    font-size: 48px;
    color: var(--ink-dark);
  }
  .brand--panel .brand-dot {
    width: 14px;
    height: 14px;
    margin: 2px 0 0 8px;
  }
  .brand--pocket {
    left: 171px;
    top: 83px;
  }
  .brand--pocket .brand-name {
    font-size: 36px;
    color: var(--ink-light);
  }
  .brand--pocket .brand-dot {
    width: 11px;
    height: 11px;
    margin: 1px 0 0 6px;
  }
</style>
</head>
<body>
  <main class="canvas">
    <h1 class="view-label">INNER WITH COLSE POCKET</h1>
    <section class="folder-inner" role="img" aria-label="Inner folder spread with a light grey hexagonal leaf-line pattern">
      <div class="brand brand--panel">
        <span class="brand-name">Tallowpeak</span>
        <span class="brand-dot"></span>
      </div>
      <div class="pocket" role="img" aria-label="Closed pocket in charcoal with a dark hexagonal leaf-line pattern">
        <div class="brand brand--pocket">
          <span class="brand-name">Tallowpeak</span>
          <span class="brand-dot"></span>
        </div>
      </div>
    </section>
  </main>
</body>
</html>
```